Clean professional design needed for landscape property business

We need a logo for a new lawncare, landscaping , property maintenance business called Meadow Trim.
Our services include lawn mowing, garden maintenance, clean ups and some property maintenance.
We want a double sided business card that is clean and very professional using the colour scheme from our logo which is provided.
the business card should have impact as we will use these to drop into people's letterboxes as a marketing drop.
Initially we want to see what you come up with so there is a very wide scope here to work with.
Updates

Project Deadline Extended
Reason: we feel our original deadline was too short. we have extended to give more time for quality submissions.

Target Market(s)

High end property owners who don't wish to do there own gardneing or property maintenance

Industry/Entity Type

Business

Contact Information for Business Card

Name
Postion/ Title
Phone number
mobile
web address
physical address

services offered

Font styles to use
Sans Serif

Requirements
Must have
• curved edges preferrred
Nice to have
• We like the idea of the logo being embossed or etched into the card so it looks like it is below the surface of the card
Should not have
• No stock images or characters.

```html
<!DOCTYPE html>
<html lang="en">
<head>
<meta charset="utf-8">
<title>Meadow Trim – Business Card</title>
<link rel="stylesheet" href="https://fonts.googleapis.com/css2?family=Montserrat:wght@500;700&family=Lato:wght@400;700&display=swap">
<style>
  :root {
    --green: #7dc142;
    --green-dark: #66a331;
    --ink: #3f4244;
    --ink-soft: #55585a;
    --card: #ffffff;
    --backdrop: #ecebe8;
  }
  * { margin: 0; padding: 0; box-sizing: border-box; }
  html, body { width: 1200px; height: 1000px; overflow: hidden; }
  body { background: var(--backdrop); position: relative; font-family: "Lato", sans-serif; }

  .card {
    position: absolute;
    background: var(--card);
    border-radius: 22px;
    overflow: hidden;
    box-shadow: 0 6px 18px rgba(0,0,0,0.18);
  }
  .card-front { left: 140px; top: 180px; width: 560px; height: 310px; }
  .card-back  { left: 480px; top: 520px; width: 515px; height: 300px; }

  .card-shape { position: absolute; inset: 0; width: 100%; height: 100%; }

  .front-brand {
    position: absolute; left: 28px; top: 138px; width: 190px;
    font-family: "Montserrat", sans-serif; font-weight: 700; font-size: 26px;
    color: #ffffff; line-height: 1.1;
  }

  .identity { position: absolute; left: 280px; top: 62px; }
  .identity-name {
    font-family: "Montserrat", sans-serif; font-weight: 700; font-size: 25px;
    color: var(--ink); letter-spacing: 0.5px;
  }
  .identity-name .accent { color: var(--green); }
  .identity-role {
    font-family: "Montserrat", sans-serif; font-weight: 500; font-size: 16px;
    color: var(--ink-soft); letter-spacing: 0.5px; margin-top: 2px;
  }

  .rule { position: absolute; left: 280px; width: 250px; height: 1.5px; background: var(--ink-soft); }
  .rule-top { top: 122px; }
  .rule-bottom { top: 216px; }

  .services { position: absolute; left: 282px; top: 134px; list-style: none; font-size: 17px; color: var(--ink-soft); line-height: 24px; }

  .contacts { position: absolute; left: 282px; top: 230px; list-style: none; font-size: 15.5px; color: var(--ink-soft); }
  .contacts li { display: flex; align-items: center; gap: 8px; height: 22px; }
  .contact-icon { width: 14px; height: 14px; flex: none; }

  .back-brand {
    position: absolute; left: 160px; top: 70px; display: flex; align-items: center; gap: 14px;
  }
  .back-brand-name {
    font-family: "Montserrat", sans-serif; font-weight: 700; font-size: 36px;
    color: var(--ink); letter-spacing: -0.5px;
  }
  .back-brand-mark { width: 14px; height: 14px; background: var(--ink); }

  .address {
    position: absolute; left: 0; right: 0; top: 248px;
    display: flex; justify-content: center; align-items: center; gap: 8px;
    font-size: 16px; color: #ffffff;
  }
  .address-icon { width: 16px; height: 16px; }
</style>
</head>
<body>

  <section class="card card-front" aria-label="Business card front">
    <svg class="card-shape" viewBox="0 0 560 310" aria-hidden="true">
      <path d="M0,0 H160 C275,45 290,240 215,310 H0 Z" fill="var(--green-dark)"/>
      <path d="M0,0 H148 C262,45 276,240 202,310 H0 Z" fill="var(--green)"/>
    </svg>
    <div class="front-brand">Meadow Trim</div>

    <div class="identity">
      <div class="identity-name">JOHN <span class="accent">DOE</span></div>
      <div class="identity-role">MANAGER</div>
    </div>
    <div class="rule rule-top"></div>
    <ul class="services">
      <li>First service goes here</li>
      <li>Second Service here</li>
      <li>Third Service here</li>
    </ul>
    <div class="rule rule-bottom"></div>
    <ul class="contacts">
      <li>
        <svg class="contact-icon" viewBox="0 0 14 14" aria-hidden="true"><circle cx="7" cy="7" r="7" fill="var(--green)"/><path d="M4.3,3.6 l1.4,0 l0.6,1.6 l-0.8,0.7 a5,5 0 0 0 2.6,2.6 l0.7,-0.8 l1.6,0.6 l0,1.4 a6.5,6.5 0 0 1 -6.1,-6.1z" fill="#fff"/></svg>
        +12 123 456 7890
      </li>
      <li>
        <svg class="contact-icon" viewBox="0 0 14 14" aria-hidden="true"><circle cx="7" cy="7" r="7" fill="var(--green)"/><rect x="3.5" y="4.5" width="7" height="5" fill="#fff"/><path d="M3.5,4.5 L7,7.3 L10.5,4.5" stroke="var(--green)" stroke-width="0.8" fill="none"/></svg>
        youremail@domain.com
      </li>
      <li>
        <svg class="contact-icon" viewBox="0 0 14 14" aria-hidden="true"><circle cx="7" cy="7" r="7" fill="var(--green)"/><circle cx="7" cy="7" r="3.6" fill="none" stroke="#fff" stroke-width="0.9"/><path d="M3.4,7 H10.6 M7,3.4 V10.6" stroke="#fff" stroke-width="0.8"/></svg>
        www.yoursite.com
      </li>
    </ul>
  </section>

  <section class="card card-back" aria-label="Business card back">
    <svg class="card-shape" viewBox="0 0 515 300" aria-hidden="true">
      <path d="M75,20 C85,60 100,100 150,140" fill="none" stroke="var(--green)" stroke-width="2.5"/>
      <path d="M0,100 C40,82 110,78 160,140 C205,178 270,180 340,168 C420,155 480,140 515,122 V300 H0 Z" fill="var(--green)"/>
    </svg>
    <div class="back-brand">
      <span class="back-brand-name">Meadow Trim</span>
      <span class="back-brand-mark"></span>
    </div>
    <div class="address">
      <svg class="address-icon" viewBox="0 0 16 16" aria-hidden="true"><circle cx="8" cy="8" r="8" fill="#fff"/><path d="M8,3.5 a2.8,2.8 0 0 1 2.8,2.8 c0,2 -2.8,5 -2.8,5 s-2.8,-3 -2.8,-5 a2.8,2.8 0 0 1 2.8,-2.8z" fill="var(--green)"/><circle cx="8" cy="6.3" r="1" fill="#fff"/></svg>
      4120 Orchard Lane, Fernbrook, PA 17344
    </div>
  </section>

</body>
</html>
```